New Business Card Design

We need a business card design for a new company based in Sydney called "Quill and Lantern". This is an online buisness which will have an online store providing imported homewares.
We are looking for something that is different, perhaps even in shape and using the logo that was designed by Tarvello Works.

Attached document is a basic example I want to see more creative versions.

Target Market(s)

Homewares, Interior Design

Industry/Entity Type

Business

Contact Information for Business Card

Company Logo
Company Name
Industry area
Name
Position
Phone
Email
Website
Motto

Requirements
Must have
• Logo
Nice to have
• Social website logos - Chatterloop, Glimmerly, Burblet, Clippadoo, Zorvo+

```html
<!DOCTYPE html>
<html lang="en">
<head>
<meta charset="utf-8">
<title>Quill and Lantern – Business Card</title>
<link rel="stylesheet" href="https://fonts.googleapis.com/css2?family=Lato:wght@400;700&display=swap">
<style>
  :root {
    --page: #e9e4dc;
    --card-top: #f7f6f3;
    --card-bottom: #e4e1db;
    --ink: #1f1f1f;
    --brown: #7a4716;
    --gold: #b98a4a;
    --band: #141414;
    --band-hi: #3a3a3a;
  }
  * { margin: 0; padding: 0; box-sizing: border-box; }
  html, body {
    width: 1200px; height: 970px; overflow: hidden;
    background: var(--page);
    font-family: "Lato", Arial, sans-serif;
    color: var(--ink);
  }
  .card {
    position: absolute; left: 172px; top: 270px;
    width: 856px; height: 476px;
    border-radius: 14px; overflow: hidden;
    background: linear-gradient(160deg, var(--card-top), var(--card-bottom));
    box-shadow: 0 10px 30px rgba(0,0,0,.18);
  }
  .brand {
    position: absolute; left: 52px; top: 132px;
    width: 350px; height: 218px;
    display: flex; align-items: center; justify-content: center;
    font-size: 38px; font-weight: 400; color: var(--ink);
    text-align: center; line-height: 1.15;
  }
  .divider {
    position: absolute; left: 423px; top: 110px;
    width: 2px; height: 256px; background: var(--brown);
  }
  .contact { position: absolute; left: 441px; top: 116px; }
  .person-name { font-size: 30px; font-weight: 700; color: var(--brown); line-height: 36px; }
  .person-role { font-size: 23px; line-height: 30px; }
  .address { margin-top: 32px; font-size: 21px; line-height: 28px; }
  .lines { margin-top: 14px; list-style: none; }
  .lines li { display: flex; align-items: center; height: 29px; font-size: 21px; }
  .lines svg { width: 20px; height: 20px; margin-right: 14px; flex: none; }
  .lines .phone { letter-spacing: 3px; }
  .rule {
    position: absolute; left: 0; top: 416px; width: 100%; height: 3px;
    background: var(--brown);
  }
  .band {
    position: absolute; left: 0; top: 424px; width: 100%; height: 52px;
    background: linear-gradient(100deg, var(--band) 0%, var(--band-hi) 30%, var(--band) 60%);
  }
  .social {
    position: absolute; right: 34px; top: 0; height: 52px;
    display: flex; align-items: center; gap: 14px; list-style: none;
  }
  .social li { display: flex; align-items: center; gap: 5px; font-size: 12px; color: var(--gold); }
  .social li::before {
    content: ""; width: 10px; height: 10px; border-radius: 50%;
    border: 2px solid var(--gold);
  }
</style>
</head>
<body>
  <div class="card">
    <div class="brand">Quill and Lantern</div>
    <div class="divider"></div>
    <div class="contact">
      <p class="person-name">Marcus Ellery</p>
      <p class="person-role">Director</p>
      <p class="address">Unit 0, Lantern Avenue<br>Quillton 1234 Queensland AU</p>
      <ul class="lines">
        <li class="phone">
          <svg viewBox="0 0 20 20"><path fill="var(--brown)" d="M2 7c0-3 3-4 8-4s8 1 8 4l-3 1-1-2H6L5 8zM5 9h10l2 8H3z"/><circle cx="10" cy="13" r="2" fill="#fff"/></svg>
          0798765432
        </li>
        <li>
          <svg viewBox="0 0 20 20"><rect x="1" y="4" width="18" height="13" fill="var(--brown)"/><path d="M1 4l9 7 9-7" fill="none" stroke="#fff" stroke-width="1.5"/></svg>
          me@quillandlantern.com.au
        </li>
        <li>
          <svg viewBox="0 0 20 20" fill="none" stroke="var(--brown)" stroke-width="1.6"><circle cx="10" cy="10" r="8"/><ellipse cx="10" cy="10" rx="3.5" ry="8"/><path d="M2 10h16M3.5 6h13M3.5 14h13"/></svg>
          www.quillandlantern.com.au
        </li>
      </ul>
    </div>
    <div class="rule"></div>
    <div class="band">
      <ul class="social">
        <li>Chatterloop</li>
        <li>Burblet</li>
        <li>Glimmerly</li>
        <li>Clippadoo</li>
        <li>Zorvo+</li>
      </ul>
    </div>
  </div>
</body>
</html>
```